Business card for acupunctist in Melbourne. Specialises in Fertility, pre and post natal care, pain

I am looking for a business card which is going to catch people eyes. Two sided, one side in a muted colour (keeping it feminine) (pink or yellow???)maybe with a little simple logo or picture, the other side I was thinking white with 3 colours (pink grey and yellow... Had these in mind.
Info on the card
Marla Quenby Acupuncture

Dr Marla Quenby (TCM Acupuncture)
Acupuncture for balancing body and mind.
Fernleaf Wellcraft
14 Corran Lane, Elsworth 3071.
94726150
0438219574
Marlatcm@quenbymail.com

Some other little logo/ designs I have liked are as follows:
http://www.dorisfelkaclinic.com/rates-and-insurance/
http://www.corinnetavish.com/
http://www.rz-needlework.co.uk/

Target Market(s)

professional women, people in pain, active people, people seeking a healthy lifefstyle.

Industry/Entity Type

Business

Font styles to use
Serif
Sans Serif

Colors
eea4c8
fde08a
aaaaaa

Requirements
Must have
• Must be eye catching, but not too loud and busy. Subltle is good. Simple is also good. The logo could be something that represents growth and health and nurturing. Again not too elaborate, very simple.
Thankyou
Should not have
• Electric colours, crazy fonts, Pictures of yin and yang, candles, or bodies.

```html
<!DOCTYPE html>
<html lang="en">
<head>
<meta charset="utf-8">
<title>Marla Quenby Acupuncture – Business Card</title>
<link rel="stylesheet" href="https://fonts.googleapis.com/css2?family=Comfortaa:wght@400;700&family=Lobster&family=Great+Vibes&display=swap">
<style>
  :root {
    --bg: #d9d9da;
    --pink: #eeaacb;
    --pink-soft: #f2bdd6;
    --yellow: #e9ec8c;
    --plum: #8b2a6c;
    --plum-light: #b0508c;
    --cream: #fbf7d2;
    --grey: #aaaaaa;
  }
  * { margin: 0; padding: 0; box-sizing: border-box; }
  html, body { width: 1200px; height: 750px; overflow: hidden; }
  body {
    background: var(--bg);
    font-family: "Comfortaa", sans-serif;
    position: relative;
  }
  .card {
    position: absolute;
    top: 222px;
    width: 510px;
    height: 306px;
    border-radius: 26px;
    overflow: hidden;
    background: var(--yellow);
    box-shadow: 0 8px 18px rgba(0,0,0,.18);
  }
  .card--front { left: 50px; }
  .card--back { left: 640px; }

  /* Front */
  .front-wave { position: absolute; inset: 0; }
  .front-mark {
    position: absolute;
    top: 22px; right: 40px;
    width: 48px; height: 48px;
    border-radius: 50%;
    background: var(--plum-light);
    opacity: .55;
  }
  .front-name {
    position: absolute;
    left: 0; right: 0; top: 150px;
    text-align: center;
    font-weight: 700;
    font-size: 27px;
    color: var(--plum);
  }
  .front-rule {
    position: absolute;
    left: 150px; right: 150px; top: 190px;
    height: 2px;
    background: var(--plum);
  }
  .front-tagline {
    position: absolute;
    left: 0; right: 0; top: 196px;
    text-align: center;
    font-family: "Lobster", cursive;
    font-size: 46px;
    color: var(--plum);
  }

  /* Back */
  .back-top {
    position: absolute;
    left: 0; right: 0; top: 0;
    height: 200px;
    background: var(--pink);
  }
  .back-divider {
    position: absolute;
    left: 232px; top: 32px;
    width: 2px; height: 150px;
    background: var(--cream);
    opacity: .8;
  }
  .contact-list {
    position: absolute;
    left: 22px; top: 52px;
    list-style: none;
    font-size: 12.5px;
    font-weight: 700;
    color: var(--yellow);
    line-height: 1.45;
  }
  .contact-list li { display: flex; align-items: flex-start; gap: 7px; margin-bottom: 4px; }
  .contact-icon {
    flex: none;
    width: 15px; height: 15px;
    border-radius: 50%;
    background: var(--plum-light);
    display: flex; align-items: center; justify-content: center;
    margin-top: 1px;
  }
  .contact-icon svg { width: 9px; height: 9px; fill: var(--cream); }
  .signature {
    position: absolute;
    left: 250px; top: 40px;
    font-family: "Great Vibes", cursive;
    font-size: 38px;
    color: var(--cream);
    text-shadow: 0 0 1px var(--plum);
  }
  .credential {
    position: absolute;
    left: 318px; top: 92px;
    font-size: 12px;
    font-weight: 700;
    color: var(--yellow);
  }
  .back-name {
    position: absolute;
    right: 26px; top: 208px;
    font-size: 30px;
    font-weight: 700;
    color: var(--plum);
    white-space: nowrap;
  }
  .back-tagline {
    position: absolute;
    right: 26px; top: 252px;
    font-size: 17px;
    color: var(--plum);
    white-space: nowrap;
  }
</style>
</head>
<body>

<section class="card card--front">
  <svg class="front-wave" viewBox="0 0 510 306" preserveAspectRatio="none" aria-hidden="true">
    <path d="M0 0 H510 V70 C420 60 330 85 240 110 C150 135 70 135 0 130 Z" fill="var(--pink)"/>
  </svg>
  <div class="front-mark"></div>
  <h1 class="front-name">Marla Quenby Acupuncture</h1>
  <div class="front-rule"></div>
  <p class="front-tagline">Fernleaf Wellcraft</p>
</section>

<section class="card card--back">
  <div class="back-top"></div>
  <div class="back-divider"></div>
  <ul class="contact-list">
    <li><span class="contact-icon"><svg viewBox="0 0 10 10"><path d="M5 0C3 0 1.6 1.5 1.6 3.4 1.6 6 5 10 5 10S8.4 6 8.4 3.4C8.4 1.5 7 0 5 0Zm0 4.8a1.4 1.4 0 1 1 0-2.8 1.4 1.4 0 0 1 0 2.8Z"/></svg></span><span>14 Corran Lane,<br>Elsworth 3071.</span></li>
    <li><span class="contact-icon"><svg viewBox="0 0 10 10"><path d="M2 0.5 3.6 2.6 2.8 3.8C3.4 5 4.9 6.6 6.2 7.2L7.4 6.4 9.5 8 8.6 9.5C5 9.4 0.6 5 0.5 1.4Z"/></svg></span><span>94726150</span></li>
    <li><span class="contact-icon"><svg viewBox="0 0 10 10"><rect x="2.5" y="0.5" width="5" height="9" rx="1"/></svg></span><span>0438219574</span></li>
    <li><span class="contact-icon"><svg viewBox="0 0 10 10"><path d="M0.5 2H9.5V8H0.5Z M0.5 2 5 5.5 9.5 2" stroke="var(--plum-light)" stroke-width=".6"/></svg></span><span>Marlatcm@quenbymail.com</span></li>
  </ul>
  <p class="signature">Dr Marla Quenby</p>
  <p class="credential">(TCM Acupuncture)</p>
  <h2 class="back-name">Marla Quenby Acupuncture</h2>
  <p class="back-tagline">Acupuncture for balancing body and mind</p>
</section>

</body>
</html>
```